Alcohol/Drug addiction treatment center and detox facility needs a billboard.

We are a new treatment center in Auburn, IN (2020), specializing in helping folks who are struggling with alcohol/drug addiction. We offer medical detox, inpatient, and outpatient care in a beautiful, safe, and stable environment, where patients will detox comfortably and then learn the coping skills necessary to lead a successful, sober life. The ad should reach people on a personal/emotional level - addicts who are overwhelmed as well as their families - reminding them that the tentacles of addiction are far-reaching; further, it should convey that you are not alone, we are committed to helping you learn how to lead a successful life, and we are here 24/7/365.
Updates

Here are some slogans that are popular in the treatment industry right now: -Your baby’s life shouldn’t begin with 1-833-HEALS-NOW (Maybe use our phone number as the last word) -Treatment Changes Everything. -Brookmere turns fear into Hope. -Pain killers are easy to get into hard to escape -It only takes a little to lose a lot. -Alcohol, Herion, Pills it all kills. -Loved one hooked on Herion? Brookmere ect. -Drive Hammered get nailed -Recovery is real -Brookmere turns fear into hope.

Target Market(s)

People struggling with addiction and their families.

Industry/Entity Type

Addiction Treatment centers

Colors

Designer to choose colors to be used in the design.

Requirements
Must have
• Brookmere Treatment; 833-HEALS-NOW; www.brookmeretreatment-example.com
Nice to have
• Catchy slogan - Examples: 1. Your baby’s life shouldn’t begin with 1-833-HEALS-Now (we could use our phone number for the last word) 2. Treatment Changes Everything. 3. It only takes a little to lose a lot. 4. Alcohol, Heroin, Pills it all kills. 5. Loved one hooked on Heroin? Brookmere can help. 6. Drive Hammered get nailed 7. Recovery is real 8. Brookmere turns fear into hope. 9. Pain killers are easy to get into hard to escape

```html
<!DOCTYPE html>
<html lang="en">
<head>
<meta charset="utf-8">
<title>Brookmere Treatment Billboard</title>
<link rel="stylesheet" href="https://fonts.googleapis.com/css2?family=Anton&family=Lexend:wght@500;600&family=Outfit:wght@700&display=swap">
<style>
  :root {
    --navy: #0d2661;
    --cyan: #00c2ef;
    --ink: #1a1a1a;
    --white: #ffffff;
    --backdrop: #e3e3e3;
    --photo-dark: #1c1612;
    --photo-warm: #5a3d2b;
  }
  html, body {
    margin: 0;
    width: 1124px;
    height: 1200px;
    overflow: hidden;
    background: var(--backdrop);
  }
  .billboard {
    position: absolute;
    left: 30px;
    top: 445px;
    width: 1064px;
    height: 309px;
    background: var(--white);
    box-shadow: 0 6px 16px rgba(0, 0, 0, 0.25);
    overflow: hidden;
  }
  .billboard svg { display: block; }
  .headline { font-family: "Anton", sans-serif; fill: var(--navy); }
  .tagline { font-family: "Outfit", sans-serif; font-weight: 700; fill: var(--white); }
  .phone-line { font-family: "Lexend", sans-serif; font-weight: 600; }
  .phone-line .label { fill: var(--navy); }
  .phone-line .number { fill: var(--ink); }
  .brand-name { font-family: "Lexend", sans-serif; font-weight: 500; fill: var(--navy); }
  .web-address { font-family: "Lexend", sans-serif; font-weight: 600; fill: var(--white); }
</style>
</head>
<body>
  <div class="billboard">
    <svg width="1064" height="309" viewBox="0 0 1064 309" xmlns="http://www.w3.org/2000/svg">
      <defs>
        <radialGradient id="photoTone" cx="60%" cy="45%" r="70%">
          <stop offset="0%" stop-color="var(--photo-warm)"/>
          <stop offset="100%" stop-color="var(--photo-dark)"/>
        </radialGradient>
      </defs>

      <!-- web address band -->
      <rect class="web-band" x="0" y="236" width="880" height="73" fill="var(--navy)"/>

      <!-- framed photo medallion -->
      <g class="medallion">
        <circle cx="904" cy="154" r="190" fill="var(--navy)"/>
        <path d="M 732 180 A 172 172 0 0 1 960 -8" fill="none" stroke="var(--cyan)" stroke-width="18"/>
        <path d="M 1076 150 A 172 172 0 0 1 1010 290" fill="none" stroke="var(--cyan)" stroke-width="18"/>
        <circle cx="904" cy="154" r="162" fill="var(--white)"/>
        <circle cx="904" cy="154" r="158" fill="url(#photoTone)" role="img"
                aria-label="Photo: a distressed woman resting her head on her hand at a table beside a bottle and a glass of whiskey"/>
      </g>

      <!-- brand -->
      <g class="brand">
        <circle cx="117" cy="78" r="36" fill="var(--cyan)"/>
        <text class="brand-name" x="117" y="156" font-size="24" text-anchor="middle" textLength="162" lengthAdjust="spacingAndGlyphs">BROOKMERE</text>
      </g>

      <!-- headline -->
      <text class="headline" x="215" y="113" font-size="116" textLength="490" lengthAdjust="spacingAndGlyphs">TREATMENT</text>

      <rect class="tagline-band" x="215" y="122" width="560" height="46" rx="10" fill="var(--cyan)"/>
      <text class="tagline" x="236" y="160" font-size="42" textLength="459" lengthAdjust="spacingAndGlyphs">CHANGES EVERYTHING</text>

      <!-- phone -->
      <text class="phone-line" x="35" y="216" font-size="31" textLength="664" lengthAdjust="spacingAndGlyphs"><tspan class="label">Brookmere Treatment: </tspan><tspan class="number">833-HEALS-NOW</tspan></text>

      <!-- web -->
      <g class="globe-icon" fill="none" stroke="var(--cyan)" stroke-width="2.5">
        <circle cx="49" cy="272" r="14"/>
        <ellipse cx="49" cy="272" rx="6" ry="14"/>
        <line x1="35" y1="272" x2="63" y2="272"/>
        <line x1="38" y1="264" x2="60" y2="264"/>
        <line x1="38" y1="280" x2="60" y2="280"/>
      </g>
      <text class="web-address" x="75" y="284" font-size="32" textLength="650" lengthAdjust="spacingAndGlyphs">www.brookmeretreatment-example.com</text>
    </svg>
  </div>
</body>
</html>
```